US company marketing to law enforcement needs brochure design

We have created a new logo and now need to update our printed material. What we really need is a "style" or "template" for how our brochures will look in the future. Enclosed is the brochure draft with the old style and logo. Also enclosed is the new logo. As we are marketing to US law enforcement it is important the the brochure design is strong, powerful and that we are looking experienced and trustworthy. However, we also want to look modern in line with the logo update.

Target Market(s)

Law enforcement

Industry/Entity Type

Marketing

```html
<!DOCTYPE html>
<html lang="en">
<head>
<meta charset="utf-8">
<title>Keystone Response – Brochure Cover</title>
<link rel="stylesheet" href="https://fonts.googleapis.com/css2?family=Source+Sans+3:wght@600&display=swap">
<style>
  :root {
    --page-bg: #e8e6e3;
    --navy: #1f386c;
    --navy-stripe-a: #243a6e;
    --navy-stripe-b: #2a2d66;
    --navy-stripe-c: #25244f;
    --navy-stripe-d: #233a6d;
    --deep-navy: #243a6b;
    --royal-blue: #0f65a8;
    --sky-blue: #3f8fd3;
    --paper: #ffffff;
    --mark-white: #ffffff;
  }
  html, body {
    margin: 0;
    padding: 0;
    width: 1200px;
    height: 1000px;
    overflow: hidden;
    background: var(--page-bg);
  }
  .brochure {
    position: absolute;
    left: 87px;
    top: 139px;
    width: 1046px;
    height: 754px;
    background: var(--paper);
    overflow: hidden;
  }
  .brochure > * { position: absolute; }

  .photo-towers {
    left: 0; top: 0; width: 510px; height: 464px;
    background: linear-gradient(95deg,
      #f2f2f2 0%, #c9c9c9 14%, #8e8e8e 30%, #5a5a5a 44%,
      #d9d9d9 56%, #7d7d7d 68%, #3f4a5a 78%, #1a5f9f 88%, #0f65a8 100%);
  }
  .stripe-deep  { left: 510px; top: 0; width: 45px; height: 281px; background: var(--deep-navy); }
  .stripe-royal { left: 555px; top: 0; width: 88px; height: 281px; background: var(--royal-blue); }
  .stripe-gap   { left: 643px; top: 0; width: 13px; height: 281px; background: var(--paper); }
  .stripe-sky   { left: 656px; top: 0; width: 21px; height: 281px; background: var(--sky-blue); }

  .photo-footsteps {
    left: 510px; top: 281px; width: 167px; height: 183px;
    background: linear-gradient(180deg, #14284a 0%, #1c3f6e 45%, #34679c 75%, #6a8fb8 100%);
  }
  .photo-portrait {
    left: 677px; top: 281px; width: 184px; height: 183px;
    background: linear-gradient(90deg, #1e1e1e 0%, #2b2b2b 40%, #555 62%, #8a8a8a 82%, #6a6a6a 100%);
  }
  .photo-facade {
    left: 861px; top: 281px; width: 185px; height: 183px;
    background: linear-gradient(115deg, #e6e6e6 0%, #a8a8a8 35%, #5e5e5e 65%, #2f2f2f 100%);
  }

  .base-band {
    left: 0; top: 464px; width: 1046px; height: 290px;
    background: var(--navy);
  }
  .base-stripe { top: 464px; height: 290px; }
  .base-stripe.s1 { left: 385px; width: 36px; background: var(--navy-stripe-a); }
  .base-stripe.s2 { left: 421px; width: 89px; background: var(--navy-stripe-b); }
  .base-stripe.s3 { left: 510px; width: 45px; background: var(--navy-stripe-c); }
  .base-stripe.s4 { left: 555px; width: 88px; background: var(--navy-stripe-b); }
  .base-stripe.s5 { left: 643px; width: 34px; background: var(--navy-stripe-d); }

  .spine-mark {
    left: 443px; top: 674px; width: 46px; height: 46px;
    border-radius: 50%; background: var(--mark-white);
  }

  .brand {
    left: 717px; top: 674px; height: 46px;
    display: flex; align-items: center; gap: 14px;
  }
  .brand-dot {
    width: 46px; height: 46px; border-radius: 50%;
    background: var(--mark-white);
  }
  .brand-name {
    font-family: "Source Sans 3", sans-serif;
    font-weight: 600;
    font-size: 27px;
    color: var(--mark-white);
    letter-spacing: -0.2px;
    white-space: nowrap;
  }
</style>
</head>
<body>
  <main class="brochure">
    <div class="photo-towers" role="img" aria-label="Dramatic black and white photo of glass office towers seen from below, tinted blue toward the spine"></div>
    <div class="stripe-deep"></div>
    <div class="stripe-royal"></div>
    <div class="stripe-gap"></div>
    <div class="stripe-sky"></div>

    <div class="photo-footsteps" role="img" aria-label="Blue-tinted photo of feet walking on pavement"></div>
    <div class="photo-portrait" role="img" aria-label="Black and white close-up portrait of a serious bearded man"></div>
    <div class="photo-facade" role="img" aria-label="Black and white photo of a glass office building facade"></div>

    <div class="base-band"></div>
    <div class="base-stripe s1"></div>
    <div class="base-stripe s2"></div>
    <div class="base-stripe s3"></div>
    <div class="base-stripe s4"></div>
    <div class="base-stripe s5"></div>

    <div class="spine-mark"></div>

    <div class="brand">
      <div class="brand-dot"></div>
      <span class="brand-name">Keystone Response</span>
    </div>
  </main>
</body>
</html>
```